Litigation Support Company Needing new Simple Web Design

I need to re-design a self done wix hosted website for a small yet nation-wide litigation support consulting firm. I built mine at www.brieflantern-hub.com myself when I launched but it is very hard on the eyes and needs refreshing/updates. Thanks for taking a look!

Target Market(s)

Law firms and technology experts in the litigation support field.

Number of Pages Required

4 page

Font styles to use
Serif

Colors
f78f20
faa54b
fac994

Requirements
Must have
• Blog, About Us, Services Pages, Crisper Graphics etc.

```html
<!DOCTYPE html>
<html lang="en">
<head>
<meta charset="utf-8">
<title>brieflantern — Litigation Support</title>
<link href="https://fonts.googleapis.com/css2?family=Montserrat:wght@300;400;500;600&family=Lato:wght@300;400;700&display=swap" rel="stylesheet">
<style>
:root{
  --orange:#f25c2a;
  --orange-light:#f78f20;
  --orange-soft:#faa54b;
  --ink:#1e1e1e;
  --text:#555;
  --muted:#8a8a8a;
  --light-bg:#f4f4f4;
  --footer:#333333;
  --white:#ffffff;
}
*{box-sizing:border-box;margin:0;padding:0}
html,body{width:1200px;height:3448px;overflow:hidden}
body{font-family:"Lato",sans-serif;color:var(--text);background:var(--white);position:relative}
.abs{position:absolute}

/* header */
.site-header{height:103px;position:relative;background:var(--white)}
.brand{position:absolute;left:120px;top:28px;display:flex;align-items:center;gap:10px;font-family:"Montserrat",sans-serif;font-size:36px;font-weight:400;color:var(--ink)}
.brand-dot{width:18px;height:18px;border-radius:50%;background:var(--orange)}
.main-nav{position:absolute;right:120px;top:44px;display:flex;gap:34px;font-family:"Montserrat",sans-serif;font-size:12px;letter-spacing:.5px;color:var(--ink)}
.main-nav .active{color:var(--orange)}

/* hero */
.hero{position:relative;height:481px;background:linear-gradient(100deg,#3d4650 0%,#5d6c7a 45%,#7d8c98 70%,#5b6672 100%);color:var(--white)}
.hero-photo{position:absolute;inset:0}
.hero-author{position:absolute;left:120px;top:82px;font-family:"Montserrat",sans-serif;font-weight:600;font-size:17px}
.hero-title{position:absolute;left:120px;top:118px;width:420px;font-family:"Montserrat",sans-serif;font-weight:400;font-size:43px;line-height:49px}
.hero-text{position:absolute;left:120px;top:282px;width:340px;font-size:15px;line-height:20px}
.btn-primary{position:absolute;left:122px;top:365px;width:253px;height:40px;border-radius:20px;background:linear-gradient(90deg,var(--orange),var(--orange-soft));color:var(--white);font-family:"Montserrat",sans-serif;font-size:13px;font-weight:600;display:flex;align-items:center;justify-content:center;gap:12px}
.hero-arrow{position:absolute;top:212px}
.hero-dots{position:absolute;left:570px;top:430px;display:flex;gap:8px}
.hero-dots span{width:12px;height:12px;border:2px solid var(--white);transform:rotate(45deg)}
.hero-dots span.on{background:var(--white)}

/* section basics */
.section-title{font-family:"Montserrat",sans-serif;font-weight:400;font-size:29px;color:var(--ink);text-align:center}
.section-sub{width:640px;margin:16px auto 0;text-align:center;font-size:15px;line-height:20px;color:var(--muted)}
.btn-outline{display:inline-flex;align-items:center;justify-content:center;border:1.5px solid #555;border-radius:14px;font-family:"Montserrat",sans-serif;font-size:9px;letter-spacing:.5px;color:var(--ink)}

/* services */
.services{height:577px;background:var(--light-bg);padding-top:96px;position:relative}
.services-rule{width:98px;height:2px;background:#555;margin:30px auto 0}
.service{position:absolute;top:272px;width:300px;text-align:center}
.service-icon{width:78px;height:78px;border-radius:50%;background:linear-gradient(180deg,var(--orange-soft),var(--orange));margin:0 auto;display:flex;align-items:center;justify-content:center;box-shadow:0 0 0 6px #fde0cf}
.service h3{margin-top:34px;font-family:"Montserrat",sans-serif;font-weight:500;font-size:17px;line-height:23px;color:var(--ink)}
.service p{margin-top:8px;font-size:13px;line-height:18px;color:var(--muted)}
.service .btn-outline{margin-top:18px;width:108px;height:27px}

/* about */
.about{position:relative;height:609px;background:var(--white)}
.about-panel{position:absolute;left:478px;top:67px;width:722px;height:467px;background:var(--orange)}
.about-photo{position:absolute;left:120px;top:129px;width:432px;height:352px;background:linear-gradient(135deg,#e9ecef 0%,#c8ced4 45%,#394454 75%,#2b3240 100%)}
.about-title{position:absolute;left:632px;top:160px;font-family:"Montserrat",sans-serif;font-weight:400;font-size:29px;color:var(--white)}
.about-rule{position:absolute;left:632px;top:205px;width:448px;height:2px;background:var(--white)}
.about-quote{position:absolute;left:632px;top:228px;width:460px;font-size:21px;line-height:27px;color:var(--white)}
.about-text{position:absolute;left:632px;top:331px;width:450px;font-size:13px;line-height:19px;color:#ffd9c6}
.about .btn-outline{position:absolute;left:632px;top:424px;width:108px;height:28px;border-color:var(--white);color:var(--white)}

/* blog */
.blog{position:relative;height:755px;background:var(--light-bg);padding-top:92px}
.post{position:absolute;width:464px;height:187px;background:var(--white);display:flex;box-shadow:0 2px 6px rgba(0,0,0,.05)}
.post-thumb{width:180px;height:100%;display:flex;align-items:center;justify-content:center;flex-shrink:0}
.post-body{padding:30px 28px 0 28px}
.post-meta{font-size:11px;color:var(--muted);padding-bottom:10px;border-bottom:1px solid #ddd;width:228px}
.post-title{margin-top:14px;font-size:16px;line-height:22px;font-weight:700;color:var(--ink)}
.post-title.link{color:var(--orange);text-decoration:underline}
.thumb-brand{font-family:"Montserrat",sans-serif;font-size:20px;color:var(--ink);display:flex;align-items:center;gap:6px}
.thumb-brand i{width:10px;height:10px;border-radius:50%;background:var(--orange)}

/* contact */
.contact{position:relative;height:568px;background:var(--white);padding-top:108px}
.contact .section-title{font-size:29px}
.field{position:absolute;height:40px;background:var(--white);box-shadow:0 1px 6px rgba(0,0,0,.09);display:flex;align-items:center;gap:10px;padding-left:18px;font-size:11px;color:#555}
.field.message{align-items:flex-start;padding-top:14px}
.btn-send{position:absolute;left:506px;top:460px;width:186px;height:42px;border-radius:21px;background:linear-gradient(90deg,var(--orange),var(--orange-soft));color:var(--white);font-family:"Montserrat",sans-serif;font-weight:600;font-size:13px;display:flex;align-items:center;justify-content:center}

/* footer */
.footer-gap{height:5px;background:var(--light-bg)}
.site-footer{position:relative;height:350px;background:var(--footer);color:#ddd;font-size:10px}
.footer-col{position:absolute;top:82px}
.footer-col h4{font-size:10px;font-weight:700;color:var(--white);margin-bottom:12px}
.footer-col li{list-style:none;line-height:14px}
.footer-col li::before{content:"› "}
.contact-line{display:flex;align-items:flex-start;gap:12px;margin-bottom:14px;line-height:13px}
.socials{display:flex;gap:6px;margin-top:12px;margin-left:72px}
.socials span{width:20px;height:20px;border:1.5px solid #ddd;border-radius:50%}
.footer-rule{position:absolute;left:340px;top:260px;width:540px;height:1px;background:#777}
.footer-brand{position:absolute;left:0;right:0;top:292px;display:flex;justify-content:center;align-items:center;gap:6px;font-family:"Montserrat",sans-serif;font-size:20px;color:var(--white)}
.footer-brand i{width:9px;height:9px;border-radius:50%;background:var(--orange)}
</style>
</head>
<body>

<header class="site-header">
  <div class="brand"><span class="brand-dot"></span>brieflantern</div>
  <nav class="main-nav">
    <span class="active">HOME</span><span>SERVICES</span><span>ABOUT US</span><span>BRIEFLANTERN BLOG</span><span>CONTACT</span>
  </nav>
</header>

<section class="hero">
  <div class="hero-photo" role="img" aria-label="Photo of an analyst reviewing data on computer monitors in a lab"></div>
  <p class="hero-author">Dana Whitcomb</p>
  <h1 class="hero-title">Don't just review investigate and discover</h1>
  <p class="hero-text">Lorem ipsum dolor sit amet, consectetur adipisicing elit, sed do eiusmod tempor incididunt ut labore et dolore magna aliqua. Ut</p>
  <a class="btn-primary">GET STARTED NOW
    <svg width="10" height="14" viewBox="0 0 10 14"><path d="M2 1l6 6-6 6" fill="none" stroke="#fff" stroke-width="2.5"/></svg></a>
  <svg class="hero-arrow" style="left:52px" width="18" height="30" viewBox="0 0 18 30"><path d="M16 2L3 15l13 13" fill="none" stroke="#fff" stroke-width="2"/></svg>
  <svg class="hero-arrow" style="left:1082px" width="18" height="30" viewBox="0 0 18 30"><path d="M2 2l13 13L2 28" fill="none" stroke="#fff" stroke-width="2"/></svg>
  <div class="hero-dots"><span></span><span class="on"></span><span></span></div>
</section>

<section class="services">
  <h2 class="section-title">Our Services</h2>
  <p class="section-sub">Lorem ipsum dolor sit amet, consectetur adipisicing elit, sed do eiusmod tempor incididunt ut labore et dolore magna aliqua. Ut enim ad minim veniam</p>
  <div class="services-rule"></div>

  <div class="service" style="left:98px">
    <div class="service-icon"><svg width="30" height="30" viewBox="0 0 30 30" fill="none" stroke="#fff" stroke-width="1.8"><rect x="7" y="4" width="16" height="22"/><path d="M11 10h8M11 15h8M11 20h5"/></svg></div>
    <h3>Received Data Discovery<br>Review Management</h3>
    <p>Lorem ipsum dolor sit amet, elit, sed<br>do eiusmod tempor ut labore dolore</p>
    <span class="btn-outline">LEARN MORE</span>
  </div>
  <div class="service" style="left:448px">
    <div class="service-icon"><svg width="30" height="30" viewBox="0 0 30 30" fill="none" stroke="#fff" stroke-width="1.8"><path d="M4 11L15 4l11 7z"/><path d="M7 12v11M12 12v11M18 12v11M23 12v11M4 25h22"/></svg></div>
    <h3>brieflantern Managed<br>Litigation Support</h3>
    <p>Lorem ipsum dolor sit amet, elit, do<br>eiusmod tempor ut labore</p>
    <span class="btn-outline">LEARN MORE</span>
  </div>
  <div class="service" style="left:775px">
    <div class="service-icon"><svg width="30" height="30" viewBox="0 0 30 30" fill="none" stroke="#fff" stroke-width="1.8"><circle cx="15" cy="8" r="4"/><path d="M15 12v6M8 18h14M8 18v4M15 18v4M22 18v4"/><circle cx="8" cy="24" r="2"/><circle cx="15" cy="24" r="2"/><circle cx="22" cy="24" r="2"/></svg></div>
    <h3>Pre-Discovery Strategy and<br>Support Services</h3>
    <p>Lorem ipsum dolor sit amet, elit, do<br>eiusmod tempor ut labore</p>
    <span class="btn-outline">LEARN MORE</span>
  </div>
</section>

<section class="about">
  <div class="about-panel"></div>
  <div class="about-photo" role="img" aria-label="Portrait photo of the company's CEO in a suit"></div>
  <h2 class="about-title">ABOUT DANA the CEO</h2>
  <div class="about-rule"></div>
  <p class="about-quote">I believe that proper application of technology can make or break the discovery process of small and large matters alike.</p>
  <p class="about-text">Document review projects can create endless headaches without proper strategy and it is my goal to analyze every project individually and apply the proper level of technology to fit the client's needs.</p>
  <span class="btn-outline">LEARN MORE</span>
</section>

<section class="blog">
  <h2 class="section-title">Latest Blog</h2>
  <p class="section-sub">Lorem ipsum dolor sit amet, consectetur adipisicing elit, sed do eiusmod tempor incididunt ut labore et dolore magna aliqua. Ut enim ad minim veniam</p>

  <article class="post" style="left:120px;top:1235px;top:235px">
    <div class="post-thumb" role="img" aria-label="Photo of a laptop, glasses and notebook on a desk" style="background:linear-gradient(135deg,#d8d4cc,#9a9184 60%,#5a5650)"></div>
    <div class="post-body">
      <p class="post-meta">01 SEP 2018 &nbsp;|&nbsp; BY DANA WHITCOMB</p>
      <p class="post-title link">Knowledge is power. Certainly an overused expression in all walks of life, but it still rings truer than</p>
    </div>
  </article>
  <article class="post" style="left:616px;top:235px">
    <div class="post-thumb"><span style="width:110px;height:46px;background:#2d2a4a;display:block" role="img" aria-label="Partner badge"></span></div>
    <div class="post-body">
      <p class="post-meta">01 SEP 2018 &nbsp;|&nbsp; BY DANA WHITCOMB</p>
      <p class="post-title">Blog text for brieflantern lorem dolor sit amet, elit, do eiusmod tempor ut labore et dolore</p>
    </div>
  </article>
  <article class="post" style="left:120px;top:450px">
    <div class="post-thumb"><span class="thumb-brand"><i></i>brieflantern</span></div>
    <div class="post-body">
      <p class="post-meta">01 SEP 2018 &nbsp;|&nbsp; BY DANA WHITCOMB</p>
      <p class="post-title">Blog text for brieflantern lorem dolor sit amet, elit, do eiusmod tempor ut labore et dolore</p>
    </div>
  </article>
  <article class="post" style="left:616px;top:450px">
    <div class="post-thumb"><span class="thumb-brand"><i></i>brieflantern</span></div>
    <div class="post-body">
      <p class="post-meta">01 SEP 2018 &nbsp;|&nbsp; BY DANA WHITCOMB</p>
      <p class="post-title">Blog text for brieflantern lorem dolor sit amet, elit, do eiusmod tempor ut labore et dolore</p>
    </div>
  </article>
</section>

<section class="contact">
  <h2 class="section-title">Contact Us</h2>
  <p class="section-sub" style="color:#333">Lorem ipsum dolor sit amet, consectetur adipisicing elit, sed do eiusmod tempor incididunt ut labore et dolore magna aliqua. Ut enim ad minim veniam</p>
  <div class="field" style="left:280px;top:244px;width:316px">
    <svg width="14" height="14" viewBox="0 0 14 14" fill="none" stroke="#999"><circle cx="7" cy="5" r="3"/><path d="M1 13c1-4 11-4 12 0"/></svg>Your Name</div>
  <div class="field" style="left:605px;top:244px;width:315px">
    <svg width="16" height="12" viewBox="0 0 16 12" fill="none" stroke="#999"><rect x="1" y="1" width="14" height="10"/><path d="M1 1l7 6 7-6"/></svg>Email</div>
  <div class="field message" style="left:280px;top:299px;width:640px;height:116px">
    <svg width="14" height="12" viewBox="0 0 14 12" fill="none" stroke="#999"><path d="M1 1h12v8H5l-3 2V9H1z"/></svg>Message</div>
  <a class="btn-send">SEND MESSAGE</a>
</section>

<div class="footer-gap"></div>
<footer class="site-footer">
  <div class="footer-col" style="left:120px">
    <h4>Getting Started</h4>
    <ul><li>Home</li><li>About Us</li><li>Services</li><li>Blog</li><li>Contact Us</li></ul>
  </div>
  <div class="footer-col" style="left:310px">
    <h4>Specialties</h4>
    <ul><li>Received Data Discovery Review Management</li><li>Managed Litigation Support</li><li>Pre-Discovery Strategy and Support Services</li></ul>
  </div>
  <div class="footer-col" style="left:660px">
    <h4>Contact Us</h4>
    <div class="contact-line"><svg width="10" height="13" viewBox="0 0 10 13" fill="#ddd"><path d="M5 0a5 5 0 0 0-5 5c0 4 5 8 5 8s5-4 5-8a5 5 0 0 0-5-5zm0 7a2 2 0 1 1 0-4 2 2 0 0 1 0 4z"/></svg><span>Lorem Ipsum Address<br>5600 Oakridge</span></div>
    <div class="contact-line"><svg width="11" height="11" viewBox="0 0 11 11" fill="#ddd"><path d="M2 0l2 3-1 1.5c.8 1.6 1.9 2.7 3.5 3.5L8 7l3 2-1 2C5 11 0 6 0 1z"/></svg><span>(555) 014-2288</span></div>
    <div class="contact-line"><svg width="12" height="9" viewBox="0 0 12 9" fill="#ddd"><path d="M0 0h12v9H0zM1 1l5 4 5-4"/></svg><span>info@brieflantern.com</span></div>
  </div>
  <div class="footer-col" style="left:888px">
    <p>© 2018 &nbsp;brieflantern Legal &amp; Privacy</p>
    <div class="socials"><span></span><span></span><span></span><span></span></div>
  </div>
  <div class="footer-rule"></div>
  <div class="footer-brand"><i></i>brieflantern</div>
</footer>

</body>
</html>
```